Business Card Design Project- Removalist

I would like to surprise my husband to be with a different type of wedding present. His brother (who he owned a removalist business with) suddenly passed away from cancer recently and he has changed his business name to 'TQB' (which stands for Keeping Ted Strong; but the full name doesn't need to be on the business card as it is more of a personal business name). To celebrate the new business I would like to get him some business cards made.
I would like the business name to be listed as 'TQB' and somewhere on the card I would like 'Sydney wide removals and relocation services'. I would like it to be obvious from the front of the card that it is a removalist business card. If a truck or some other feature that makes it look like a removalist business card could added it would be appreciated.
I don't mind what colours are used, but I would like the colour blue to feature somewhere in the design. It can be bright and fun, which is how Ted was.
I will also need the company's email address and phone number listed
The email address is: tqbmoving@brisketmail.example
The contact number is: 0418 902 364
I don't need a contact name listed on the card, but perhaps 'Owned and operated by the Pemberton family' could be added near the contact details in small font.
Thank you very much for considering this project!
Kind regards,
Fiona
Updates
Could you please change the mobile contact number to 0418 902 364. This is the only contact phone number required on the card now.
Thank you!
Industry/Entity Type
Wedding
Look and feel
Each slider illustrates characteristics of the customer's brand and the style your logo design should communicate.

```html
<!DOCTYPE html>
<html lang="en">
<head>
<meta charset="utf-8">
<title>TQB – Business Card</title>
<link rel="stylesheet" href="https://fonts.googleapis.com/css2?family=Arimo:wght@400;700&display=swap">
<style>
  :root {
    --card-blue: #386594;
    --truck-tone: #4a76a3;
    --ink: #ffffff;
  }
  * { margin: 0; padding: 0; box-sizing: border-box; }
  html, body {
    width: 1200px;
    height: 667px;
    overflow: hidden;
    background: var(--card-blue);
  }
  .card {
    position: relative;
    width: 1200px;
    height: 667px;
    overflow: hidden;
    background: var(--card-blue);
    color: var(--ink);
    font-family: "Arimo", Arial, sans-serif;
  }
  .truck-illustration {
    position: absolute;
    left: 745px;
    top: 110px;
    width: 325px;
    height: 220px;
    background: linear-gradient(180deg, var(--truck-tone), var(--card-blue));
    border-radius: 6px;
  }
  .brand-name {
    position: absolute;
    left: 203px;
    top: 131px;
    font-size: 160px;
    line-height: 1;
    font-weight: 700;
    letter-spacing: 20px;
    white-space: nowrap;
  }
  .tagline {
    position: absolute;
    left: 135px;
    top: 294px;
    font-size: 26.5px;
    line-height: 1.1;
    font-weight: 700;
    white-space: nowrap;
  }
  .ground-line {
    position: absolute;
    left: 58px;
    top: 326px;
  }
  .contact-row {
    position: absolute;
    left: 70px;
    display: flex;
    align-items: center;
    gap: 12px;
    white-space: nowrap;
  }
  .contact-row.phone { top: 440px; }
  .contact-row.email { top: 528px; }
  .contact-text {
    font-size: 47px;
    line-height: 1;
    font-weight: 400;
  }
  .owner-note {
    position: absolute;
    left: 70px;
    top: 604px;
    font-size: 22px;
    line-height: 1.1;
    font-weight: 400;
  }
</style>
</head>
<body>
  <div class="card">
    <div class="truck-illustration" role="img" aria-label="Hand-sketched white line drawing of a removal truck"></div>

    <div class="brand-name">TQB</div>
    <div class="tagline">Sydney wide removals and relocation services</div>

    <svg class="ground-line" width="1075" height="14" viewBox="0 0 1075 14" aria-hidden="true">
      <path d="M0 8 Q 540 3 1072 5 L1072 8 Q 540 7 0 9 Z" fill="#ffffff"/>
    </svg>

    <div class="contact-row phone">
      <svg width="80" height="80" viewBox="0 0 80 80" aria-hidden="true">
        <circle cx="40" cy="40" r="37" fill="none" stroke="#ffffff" stroke-width="3"/>
        <path d="M30 20 l8 10 -5 5 q4 10 14 16 l5 -5 10 8 -6 7 q-20 -2 -33 -27 q-2 -8 7 -14 z"
              fill="none" stroke="#ffffff" stroke-width="3" stroke-linejoin="round"/>
      </svg>
      <span class="contact-text">0418 902 364</span>
    </div>

    <div class="contact-row email">
      <svg width="80" height="56" viewBox="0 0 80 56" aria-hidden="true">
        <rect x="2" y="2" width="76" height="52" rx="3" fill="none" stroke="#ffffff" stroke-width="3"/>
        <path d="M4 5 L40 34 L76 5 M4 52 L30 27 M76 52 L50 27" fill="none" stroke="#ffffff" stroke-width="3"/>
      </svg>
      <span class="contact-text">tqbmoving@brisketmail.example</span>
    </div>

    <div class="owner-note">Owned and operated by the Pemberton family</div>
  </div>
</body>
</html>
```